TRQ Harbor Gym Team starting a weekly fitness and wellness podcast.

We need to design both a program advert poster for socials and campaigns as well as a podcast placeholder/poster.
The podcast is part of an online group training program called "Summit Stride".
The four pillars of Summit Stride are Fitness, Nutrition, Mindset & Community.
The program is designed and owned by TRQ Harbor Gym.
The brand guidelines are similar to TRQ Harbor Gym (Attached).
Target Market(s)
People aged between 30 and 60yrs old new or returning to fitness and wellness
Industry/Entity Type
Fitness
Colors
Designer to choose colors to be used in the design.
Requirements
Must have
- A strong motivational appeal. One that inspires and motivates people to take action.
Nice to have
- a captivating caption
Should not have
- Too much Zen or yoga themes.

```html
<!DOCTYPE html>
<html lang="en">
<head>
<meta charset="UTF-8">
<title>Summit Stride Podcast</title>
<link href="https://fonts.googleapis.com/css2?family=Poppins:ital,wght@0,500;0,600;0,700;1,700;1,800&display=swap" rel="stylesheet">
<style>
  :root {
    --teal: #05adbb;
    --violet: #8a68a8;
    --magenta: #df3b96;
    --coral: #ea5a5c;
    --orange: #fb7a08;
    --white: #ffffff;
    --ink: #111111;
    --panel: rgba(255, 255, 255, 0.22);
  }
  * { margin: 0; padding: 0; box-sizing: border-box; }
  html, body { width: 1200px; height: 1200px; overflow: hidden; background: var(--white); }
  body { font-family: "Poppins", sans-serif; color: var(--white); }

  .canvas {
    position: relative;
    width: 1200px;
    height: 1200px;
    background: var(--white);
    border: 1px solid var(--ink);
  }
  .poster {
    position: absolute;
    left: 62px; top: 62px;
    width: 1076px; height: 1076px;
    background: linear-gradient(135deg,
      var(--teal) 0%, var(--teal) 14%,
      var(--violet) 36%, var(--magenta) 56%,
      var(--coral) 70%, var(--orange) 86%, var(--orange) 100%);
  }
  .shapes { position: absolute; left: 0; top: 0; width: 1200px; height: 1200px; }

  .abs { position: absolute; line-height: 1; white-space: nowrap; }

  .brand-name { left: 238px; top: 147px; font-size: 28px; font-weight: 700; }

  .gym-badge {
    position: absolute;
    left: 938px; top: 116px; width: 116px; height: 91px;
    background: var(--white);
    border-radius: 30px;
    display: flex; align-items: center; justify-content: center;
    text-align: center;
    font-size: 17px; font-weight: 700; line-height: 1.15;
    color: var(--magenta);
  }

  .title { font-size: 100px; font-weight: 600; letter-spacing: -1px; }
  .title-line-1 { left: 142px; top: 265px; }
  .title-line-2 { left: 146px; top: 384px; }

  .pillars-intro { left: 162px; top: 533px; font-size: 27px; font-weight: 600; }

  .pillar-label {
    position: absolute; top: 749px; width: 200px; margin-left: -100px;
    text-align: center; font-size: 22px; font-weight: 600; line-height: 1;
  }

  .tagline { left: 194px; top: 838px; font-size: 36px; font-weight: 600; display: flex; align-items: baseline; }
  .tagline .word { text-decoration: underline; text-decoration-thickness: 3px; text-underline-offset: 9px; }
  .tagline .best-self { position: relative; margin-left: 34px; font-weight: 800; font-style: italic; }
  .tagline .best-self svg { position: absolute; left: -18px; top: -17px; width: 214px; height: 80px; overflow: visible; }

  .available { left: 718px; top: 981px; font-size: 26px; font-weight: 600; display: flex; align-items: center; gap: 10px; }
  .platforms { font-size: 16px; font-weight: 700; display: flex; align-items: center; gap: 7px; }
  .platform-dot { width: 12px; height: 12px; border-radius: 50%; background: var(--white); }

  .episode-link {
    left: 718px; top: 1025px; font-size: 26px; font-weight: 700; font-style: italic;
    text-decoration: underline; text-decoration-thickness: 2px; text-underline-offset: 5px;
  }
</style>
</head>
<body>
<div class="canvas">
  <div class="poster"></div>

  <svg class="shapes" viewBox="0 0 1200 1200" aria-hidden="true">
    <!-- brand mark circle and header rule -->
    <circle cx="184" cy="161" r="40" fill="#fff"/>
    <rect x="596" y="160" width="301" height="3" fill="#fff"/>

    <!-- microphone badge -->
    <circle cx="653" cy="436" r="63" fill="#fff"/>
    <g fill="none" stroke="var(--magenta)" stroke-width="5" stroke-linecap="round">
      <rect x="639" y="393" width="28" height="60" rx="14" fill="var(--violet)" stroke="none"/>
      <path d="M632 437 Q632 456 653 456 Q674 456 674 437"/>
      <line x1="653" y1="456" x2="653" y2="476"/>
      <line x1="640" y1="476" x2="666" y2="476"/>
    </g>

    <!-- pillars panel -->
    <rect x="146" y="580" width="861" height="212" rx="40" fill="var(--panel)" stroke="#fff" stroke-width="4"/>
    <g stroke="#fff" stroke-width="4">
      <line x1="366" y1="594" x2="366" y2="777"/>
      <line x1="576" y1="594" x2="576" y2="777"/>
      <line x1="791" y1="594" x2="791" y2="777"/>
    </g>
    <g fill="none" stroke="#fff" stroke-width="3.5">
      <circle cx="260" cy="668" r="66"/>
      <circle cx="472" cy="668" r="66"/>
      <circle cx="683" cy="668" r="66"/>
      <circle cx="899" cy="668" r="66"/>
    </g>
    <!-- fitness: dumbbell -->
    <g fill="#fff">
      <rect x="219" y="666" width="82" height="6"/>
      <rect x="226" y="647" width="14" height="42"/>
      <rect x="281" y="647" width="14" height="42"/>
      <rect x="219" y="655" width="9" height="24"/>
      <rect x="293" y="655" width="9" height="24"/>
    </g>
    <!-- nutrition: person with heart -->
    <g fill="#fff">
      <circle cx="472" cy="644" r="11"/>
      <path d="M472 701 L449 679 Q441 670 450 662 Q459 655 467 664 L472 669 L477 664 Q485 655 494 662 Q503 670 495 679 Z"/>
    </g>
    <!-- community: group -->
    <g fill="#fff">
      <circle cx="683" cy="650" r="11"/>
      <circle cx="661" cy="656" r="9"/>
      <circle cx="705" cy="656" r="9"/>
      <rect x="670" y="665" width="26" height="31" rx="9"/>
      <path d="M654 670 L665 668 L665 695 Q655 694 653 684 Z"/>
      <path d="M712 670 L701 668 L701 695 Q711 694 713 684 Z"/>
    </g>
    <!-- mindset: head -->
    <g>
      <path d="M880 697 L880 682 Q871 674 871 660 Q872 638 893 638 Q911 638 917 652 L922 671 L915 673 L915 681 Q915 687 908 687 L906 687 L906 697 Z" fill="#fff"/>
      <rect x="887" y="656" width="5" height="11" fill="var(--magenta)"/>
      <rect x="896" y="651" width="5" height="22" fill="var(--magenta)"/>
      <rect x="905" y="656" width="5" height="11" fill="var(--magenta)"/>
    </g>

    <!-- footer rule -->
    <rect x="145" y="1013" width="518" height="3" fill="#fff"/>
  </svg>

  <div class="abs brand-name">Summit Stride Podcast</div>

  <div class="gym-badge">TRQ Harbor<br>Gym</div>

  <h1 class="abs title title-line-1">Summit Stride</h1>
  <div class="abs title title-line-2">Podcast</div>

  <p class="abs pillars-intro">The four pillars of Summit Stride are :</p>

  <span class="pillar-label" style="left:260px">FITNESS</span>
  <span class="pillar-label" style="left:472px">NUTRITION</span>
  <span class="pillar-label" style="left:683px">COMMUNITY</span>
  <span class="pillar-label" style="left:899px">MINDSET</span>

  <p class="abs tagline">
    <span class="word">Listen</span>,&nbsp;<span class="word">Learn</span>,&nbsp;and&nbsp;<span class="word">Chase</span>&nbsp;Your
    <span class="best-self">Best Self!
      <svg viewBox="0 0 214 80" aria-hidden="true">
        <ellipse cx="107" cy="40" rx="104" ry="36" fill="none" stroke="#fff" stroke-width="2.5"/>
        <ellipse cx="108" cy="39" rx="102" ry="33" fill="none" stroke="#fff" stroke-width="1.5" transform="rotate(-1.5 107 40)"/>
      </svg>
    </span>
  </p>

  <div class="abs available">Available On :
    <span class="platforms"><span class="platform-dot"></span>ViewCast · TuneWave</span>
  </div>
  <div class="abs episode-link">Summit Stride Podcast</div>
</div>
</body>
</html>
```